Brake Caliper Box Design - 4 Sizes

We need new packaging design for our products. We are a company based in Montreal, Quebec and we re-manufacture calipers. This project requires that 4 box sizes be designed (same overall design). The boxes need to be bilingual (French and English). Our products are top quality premium products and the boxes should reflect that, we want something modern, very professional and it needs to be much more refined and polished than our previous design. 3D renders would be much appreciated.

The text in the previous design is to be re-used, also the new design should incorporate two badges (Gaurantee and Certified badge)

I have included our previous design for reference only. This design MUST be completely different. You will need to design a logo for this box.

We need the designs delivered in .eps and .jpg format.

******** Update ************

We still think some people have misunderstood what brand they are designing boxes for. We need boxes designed for a new brand called "ZOR Meridian". Along with the boxes we need a logo for this new brand. The logo and box design CANNOT LOOK, FEEL and BE anything like the sample box designs we provided. These sample box designs were supplied only for size and to provide text/images for the new design (besides the LOGO).

Target Market(s)

Auto Part Stores

Logo Text

ZOR MERIDIAN

Requirements
Must have
• caliper pictures, 2 year Gaurantee badge and Certified badge

```html
<!DOCTYPE html>
<html lang="fr">
<head>
<meta charset="utf-8">
<title>ZOR Meridian – Disc Brake Caliper Box</title>
<link href="https://fonts.googleapis.com/css2?family=Oswald:wght@400;500;600;700&family=Roboto+Condensed:ital,wght@0,400;0,700;1,700&display=swap" rel="stylesheet">
<style>
  :root {
    --bg: #c4c4c4;
    --black: #161616;
    --black-soft: #222222;
    --green: #7aa73a;
    --green-dark: #3f5c1d;
    --white: #ffffff;
    --grey-text: #bdbdbd;
    --silver-light: #f2f2f2;
    --silver-dark: #9a9a9a;
    --badge: #8a8a8a;
  }
  * { margin: 0; padding: 0; box-sizing: border-box; }
  html, body {
    width: 1200px; height: 844px; overflow: hidden;
    background: var(--bg);
    font-family: "Roboto Condensed", Arial, sans-serif;
  }
  .box-dieline {
    position: absolute; left: 180px; top: 222px;
    width: 840px; height: 400px;
    display: flex;
  }
  .side-panel, .front-panel { position: relative; height: 400px; overflow: hidden; }
  .side-panel { width: 200px; background: var(--black-soft); }
  .front-panel { width: 640px; background: var(--black); }
  .panel-art { position: absolute; inset: 0; }

  /* side panel */
  .side-header {
    position: absolute; left: 12px; top: 22px; right: 10px;
    display: flex; align-items: center; gap: 5px;
  }
  .side-header .mini-badge { width: 15px; height: 15px; border-radius: 50%; background: var(--badge); flex: none; }
  .side-header p { color: var(--white); font-size: 7px; line-height: 1.25; font-weight: 700; }
  .side-copy {
    position: absolute; left: 12px; top: 62px; right: 12px;
    color: var(--grey-text); font-size: 7.4px; line-height: 1.55;
  }
  .side-brand {
    position: absolute; left: 12px; top: 318px;
    display: flex; align-items: center; gap: 5px;
  }
  .side-product {
    position: absolute; left: 12px; top: 342px;
    color: var(--black); font-size: 10.5px; line-height: 1.25; font-weight: 700;
  }
  .side-product em { font-style: italic; }

  /* brand mark */
  .brand { display: flex; align-items: center; gap: 8px; }
  .brand-dot { border-radius: 50%; background: var(--white); flex: none; }
  .brand-name {
    font-family: "Oswald", Arial, sans-serif; font-weight: 600;
    color: var(--white); letter-spacing: 1px; white-space: nowrap;
  }
  .side-brand .brand-dot { width: 10px; height: 10px; background: var(--black); }
  .side-brand .brand-name { font-size: 12px; color: var(--black); }
  .front-brand { position: absolute; left: 40px; top: 44px; }
  .front-brand .brand-dot { width: 22px; height: 22px; }
  .front-brand .brand-name { font-size: 30px; }

  /* front panel */
  .caliper-photo {
    position: absolute; left: 340px; top: 70px; width: 250px; height: 230px;
    border-radius: 40px;
    background: radial-gradient(ellipse at 45% 40%, #c9c9c9 0%, #8d8d8d 55%, #5b5b5b 100%);
  }
  .badges { position: absolute; right: 40px; top: 24px; display: flex; gap: 14px; }
  .badge { width: 40px; height: 40px; border-radius: 50%; background: var(--badge); border: 2px solid var(--silver-light); }
  .return-note {
    position: absolute; right: 40px; top: 74px; text-align: right;
    color: var(--grey-text); font-size: 6.5px; line-height: 1.35;
  }
  .product-title {
    position: absolute; left: 40px; top: 322px;
    font-family: "Roboto Condensed", Arial, sans-serif; font-weight: 700;
    color: var(--black); line-height: 1.15;
  }
  .product-title .fr { font-size: 20px; display: block; }
  .product-title .en { font-size: 20px; font-style: italic; display: block; }
  .size-label {
    position: absolute; left: 548px; top: 336px; width: 110px;
    transform: rotate(-45deg); text-align: center;
    font-family: "Oswald", Arial, sans-serif; font-weight: 700; font-size: 19px;
    color: var(--black); letter-spacing: 1px;
  }
</style>
</head>
<body>
<main class="box-dieline">
  <section class="side-panel">
    <svg class="panel-art" width="200" height="400" viewBox="0 0 200 400">
      <polygon points="0,236 200,256 200,270 0,250" fill="var(--green-dark)"/>
      <polygon points="0,250 200,270 200,400 0,400" fill="var(--green)"/>
    </svg>
    <div class="side-header">
      <span class="mini-badge"></span><span class="mini-badge"></span>
      <p>Qualité garantie | Éprouvé à 100%<br>100% Pretested for Guaranteed Quality</p>
    </div>
    <p class="side-copy">Chaque étrier est remis à neuf, nettoyé, inspecté et testé sous pression pour offrir un freinage sûr et constant. Every caliper is rebuilt, cleaned, inspected and pressure tested to deliver safe, consistent braking. Installation par un technicien qualifié recommandée. Professional installation recommended.</p>
    <div class="side-brand brand"><span class="brand-dot"></span><span class="brand-name">ZOR MERIDIAN</span></div>
    <p class="side-product">Étrier de frein à disques<br><em>Disc Brake Caliper</em></p>
  </section>

  <section class="front-panel">
    <svg class="panel-art" width="640" height="400" viewBox="0 0 640 400">
      <polygon points="0,282 640,158 640,176 0,300" fill="var(--green-dark)"/>
      <polygon points="0,300 640,176 640,400 0,400" fill="var(--green)"/>
      <defs>
        <linearGradient id="silver-band" x1="0" y1="0" x2="1" y2="1">
          <stop offset="0" stop-color="var(--silver-light)"/>
          <stop offset="1" stop-color="var(--silver-dark)"/>
        </linearGradient>
      </defs>
      <polygon points="532,400 640,292 640,338 578,400" fill="url(#silver-band)"/>
    </svg>
    <div class="front-brand brand"><span class="brand-dot"></span><span class="brand-name">ZOR MERIDIAN</span></div>
    <div class="caliper-photo" role="img" aria-label="Photo of a remanufactured disc brake caliper"></div>
    <div class="badges">
      <span class="badge" role="img" aria-label="Certified badge"></span>
      <span class="badge" role="img" aria-label="2 year guarantee badge"></span>
    </div>
    <p class="return-note">Pour les conditions de remboursement, voir le dessous<br>For returning conditions, look under the box</p>
    <h1 class="product-title">
      <span class="fr">Étrier de frein à disques</span>
      <span class="en">Disc Brake Caliper</span>
    </h1>
    <div class="size-label">SMALL</div>
  </section>
</main>
</body>
</html>
```